Vantage Systemworks Brochure

We are looking to design a trifold sales brochure for a building automation company. We focus on selling and installing Quorvex open protocol building management systems. We would like to design this around our black and red color scheme. Our company is based in Belmont Michigan just outside of Grand Rapids. Our Customer base is strictly commercial and industrial buildings no residential. Attached is a powerpoint with more of our company information.

```html
<!DOCTYPE html>
<html lang="en">
<head>
<meta charset="utf-8">
<title>Vantage Systemworks Brochure</title>
<link href="https://fonts.googleapis.com/css2?family=Montserrat:wght@400;500;600;700;800&display=swap" rel="stylesheet">
<style>
:root{
  --red:#e8393f;
  --black:#000;
  --ink:#111;
  --white:#fff;
  --paper:#fff;
  --muted:#444;
}
*{margin:0;padding:0;box-sizing:border-box}
html,body{width:1200px;height:789px;overflow:hidden;background:var(--paper)}
body{position:relative;font-family:'Montserrat',sans-serif;color:var(--ink)}
.spread{position:absolute;top:35px;width:553px;height:715px;box-shadow:0 0 4px rgba(0,0,0,.12)}
.spread--outer{left:37px}
.spread--inner{left:614px}
.shapes{position:absolute;left:0;top:0;width:553px;height:715px}
.panel{position:absolute;top:0;width:184.5px;height:715px}
.p1{left:0}.p2{left:184.5px}.p3{left:369px}
.abs{position:absolute}
.heading{font-weight:700;font-size:16px;letter-spacing:.2px;line-height:1;white-space:nowrap}
.tag{background:var(--red);color:var(--white);padding:4px 4px 5px;display:inline-block}
.company-text{left:10px;top:112px;width:168px;font-size:6.1px;line-height:15.6px;font-weight:500}
.company-text p+p{margin-top:7px}
.contact-title{left:40px;top:176px;color:var(--red);font-size:20px;font-weight:700;font-variant:small-caps;letter-spacing:.5px}
.c-label{left:40px;color:var(--white);font-size:8px;font-weight:700}
.c-rule{left:40px;width:120px;height:1px;background:#bbb}
.c-line{left:40px;color:var(--white);font-size:6.6px;font-weight:600}
.social{left:40px;top:500px;display:flex;gap:2px}
.social span{width:16px;height:16px;border:1px solid var(--red);border-radius:50%;background:#111}
.brand{left:0;width:184.5px;top:32px;text-align:center}
.brand-name{display:inline-flex;align-items:center;gap:5px;font-weight:800;font-size:10.5px;letter-spacing:.3px}
.brand-name i{width:12px;height:12px;border-radius:50%;background:var(--red);display:inline-block}
.brand-sub{font-size:4.5px;margin-top:4px;font-weight:500}
.welcome{left:0;width:184.5px;text-align:center}
.url-box{left:12px;top:619px;width:160px;height:33px;border:2px solid var(--red);display:flex;background:var(--white)}
.url-box .globe{width:34px;background:var(--red);display:flex;align-items:center;justify-content:center}
.url-box .url{flex:1;display:flex;align-items:center;justify-content:center;font-size:6.6px;font-weight:600}
.cust{width:84px;text-align:center;font-size:6.3px;font-weight:700;color:#333;line-height:1.2;display:flex;align-items:center;justify-content:center;gap:3px}
.cust i{width:6px;height:6px;background:#333;flex:none}
.svc-head{left:0;width:184.5px;text-align:center;color:var(--white);font-size:16px;font-weight:700;line-height:30px;top:70px}
.svc-cat{color:var(--white);font-size:12.5px;font-weight:700;line-height:24px}
.svc-list{left:14px;color:var(--white);font-size:8.2px;font-weight:600;list-style:none}
.svc-list li{position:relative;padding-left:9px;line-height:22.3px}
.svc-list li::before{content:"»";position:absolute;left:0;font-size:7px}
.svc-list .cont{padding-left:9px}
.svc-list .cont::before{content:""}
.benefit{left:31px;font-size:10.5px;font-weight:600;line-height:17px;white-space:nowrap}
.b-icon{left:1px;width:20px;height:20px}
</style>
</head>
<body>

<section class="spread spread--outer">
  <svg class="shapes" viewBox="0 0 553 715" aria-hidden="true">
    <rect width="553" height="715" fill="var(--white)"/>
    <!-- company panel -->
    <polygon points="0,408 184.5,325 184.5,715 0,715" fill="url(#bldgDark)" role="img" aria-label="Photo of a modern dark-clad office building entrance under a pale sky"/>
    <polygon points="0,349 54,374 0,399" fill="var(--black)"/>
    <polygon points="114,715 184.5,681 184.5,715" fill="var(--red)"/>
    <!-- contact panel -->
    <rect x="184.5" width="184.5" height="715" fill="var(--black)"/>
    <!-- cover panel -->
    <polygon points="369,84 450,119 369,159" fill="var(--red)"/>
    <polygon points="369,170 553.5,82 553.5,376 369,461" fill="url(#towerBlue)" role="img" aria-label="Photo of glass office towers against a blue sky"/>
    <polygon points="553.5,387 513,406 553.5,424" fill="var(--black)"/>
    <defs>
      <linearGradient id="bldgDark" x1="0" y1="0" x2="0" y2="1">
        <stop offset="0" stop-color="#c6d6e6"/>
        <stop offset=".35" stop-color="#4a5260"/>
        <stop offset=".8" stop-color="#2a2e35"/>
        <stop offset="1" stop-color="#9aa0a8"/>
      </linearGradient>
      <linearGradient id="towerBlue" x1="0" y1="0" x2="1" y2="1">
        <stop offset="0" stop-color="#8fb4d6"/>
        <stop offset=".5" stop-color="#4e6f8c"/>
        <stop offset="1" stop-color="#2c3f52"/>
      </linearGradient>
    </defs>
  </svg>

  <div class="panel p1">
    <div class="abs heading" style="left:19px;top:58px">OUR <span class="tag">COMPANY</span></div>
    <div class="abs company-text">
      <p>Vantage Systemworks is a division of Harlan Mechanical, West Michigan’s largest full service mechanical contractors for over 40 years. We focus on building long term relationships with our customers by providing a next level building automation experience. Our fulltime team of engineers and electricians are trained on mechanical and controls systems to make sure your building management system is performing at its full potential.</p>
      <p>Our focus is growth through commitment to service and sustainability.</p>
    </div>
  </div>

  <div class="panel p2">
    <div class="abs contact-title">Contact</div>
    <div class="abs c-label" style="top:233px">PHONE &amp; FAX</div>
    <div class="abs c-rule" style="top:250px"></div>
    <div class="abs c-line" style="top:266px">PHONE : +1 555 014 2290</div>
    <div class="abs c-line" style="top:286px">FAX : +1 555 014 2291</div>
    <div class="abs c-label" style="top:319px">MAIL &amp; WEB</div>
    <div class="abs c-rule" style="top:337px"></div>
    <div class="abs c-line" style="top:353px">MAIL : HELLO@VANTAGESW.NET</div>
    <div class="abs c-line" style="top:372px">WEB : WWW.VANTAGESW.NET</div>
    <div class="abs c-label" style="top:404px">ADDRESS</div>
    <div class="abs c-rule" style="top:421px"></div>
    <div class="abs c-line" style="top:437px">418 BIRCHLINE AVE, SUITE 20</div>
    <div class="abs c-line" style="top:453px">BELMONT, MICHIGAN</div>
    <div class="abs c-line" style="top:468px">49306</div>
    <div class="abs social" aria-label="Social media"><span></span><span></span><span></span><span></span><span></span></div>
  </div>

  <div class="panel p3">
    <div class="abs brand">
      <div class="brand-name"><i></i>VANTAGE SYSTEMWORKS</div>
      <div class="brand-sub">A Division of Harlan Mechanical</div>
    </div>
    <div class="abs welcome heading" style="top:498px">WELCOME TO</div>
    <div class="abs welcome" style="top:528px"><span class="heading tag" style="padding:5px 10px 7px">VANTAGE</span></div>
    <div class="abs welcome heading" style="top:573px">SYSTEMWORKS</div>
    <div class="abs url-box">
      <div class="globe">
        <svg width="18" height="18" viewBox="0 0 20 20" fill="none" stroke="#fff" stroke-width="1.2"><circle cx="10" cy="10" r="8"/><ellipse cx="10" cy="10" rx="3.5" ry="8"/><line x1="2" y1="10" x2="18" y2="10"/><line x1="3.5" y1="6" x2="16.5" y2="6"/><line x1="3.5" y1="14" x2="16.5" y2="14"/></svg>
      </div>
      <div class="url">WWW.VANTAGESYSTEMWORKS.COM</div>
    </div>
  </div>
</section>

<section class="spread spread--inner">
  <svg class="shapes" viewBox="0 0 553 715" aria-hidden="true">
    <rect width="553" height="715" fill="var(--white)"/>
    <polygon points="0,408 184.5,325 184.5,715 0,715" fill="url(#skyUp)" role="img" aria-label="Photo looking up between glass skyscrapers"/>
    <polygon points="0,349 54,374 0,399" fill="var(--black)"/>
    <polygon points="114,715 184.5,681 184.5,715" fill="var(--red)"/>
    <rect x="184.5" width="184.5" height="715" fill="var(--red)"/>
    <polygon points="369,325 553.5,408 553.5,715 369,715" fill="url(#glassBlue)" role="img" aria-label="Photo of a blue glass office building corner"/>
    <polygon points="553.5,349 484,374 553.5,399" fill="var(--black)"/>
    <polygon points="369,681 440,715 369,715" fill="var(--red)"/>
    <defs>
      <linearGradient id="skyUp" x1="0" y1="0" x2="1" y2="1">
        <stop offset="0" stop-color="#6a5a5e"/>
        <stop offset=".45" stop-color="#c9d3dc"/>
        <stop offset="1" stop-color="#2f4457"/>
      </linearGradient>
      <linearGradient id="glassBlue" x1="0" y1="0" x2="1" y2="1">
        <stop offset="0" stop-color="#a9cdf0"/>
        <stop offset=".5" stop-color="#2f78c8"/>
        <stop offset="1" stop-color="#1b4f8c"/>
      </linearGradient>
    </defs>
  </svg>

  <div class="panel p1">
    <div class="abs heading" style="left:8px;top:36px">SOME OF OUR KEY</div>
    <div class="abs heading" style="left:33px;top:61px"><span class="tag">CUSTOMERS</span></div>
    <div class="abs cust" style="left:6px;top:118px"><i></i>Norhaven Outfitters</div>
    <div class="abs cust" style="left:96px;top:118px"><i></i>Calder Heatworks</div>
    <div class="abs cust" style="left:6px;top:157px"><i></i>Lakeshore Hall</div>
    <div class="abs cust" style="left:96px;top:157px"><i></i>Brightwater Arena</div>
    <div class="abs cust" style="left:6px;top:192px"><i></i>Dunmore Shores Schools</div>
    <div class="abs cust" style="left:96px;top:192px"><i></i>Pinecrest Public Schools</div>
    <div class="abs cust" style="left:6px;top:231px"><i></i>Tidwell Home Care</div>
    <div class="abs cust" style="left:96px;top:231px"><i></i>Ridgeport College</div>
    <div class="abs cust" style="left:6px;top:267px"><i></i>Meadowfield Dairy</div>
    <div class="abs cust" style="left:96px;top:267px"><i></i>Kestrel Foods</div>
    <div class="abs cust" style="left:6px;top:301px"><i></i>Harbor Area Schools</div>
    <div class="abs cust" style="left:96px;top:305px"><i></i>Oakvale College</div>
  </div>

  <div class="panel p2">
    <div class="abs svc-head">SERVICES WE<br>OFFER</div>
    <svg class="abs" style="left:15px;top:158px" width="32" height="36" viewBox="0 0 32 36" fill="none" stroke="#fff" stroke-width="1.3">
      <polyline points="2,16 16,3 30,16"/><rect x="6" y="14" width="20" height="18"/><line x1="2" y1="34" x2="30" y2="34"/>
      <circle cx="16" cy="22" r="4"/><circle cx="16" cy="22" r="7" stroke-dasharray="2.5 2"/>
    </svg>
    <div class="abs" style="left:51px;top:158px;width:1px;height:36px;background:#fff"></div>
    <div class="abs svc-cat" style="left:67px;top:152px">BUILDING<br>AUTOMATION</div>
    <ul class="abs svc-list" style="top:212px">
      <li>QUORVEX BASE BUILDING</li>
      <li class="cont">AUTOMATION SYSTEMS</li>
      <li>OPEN UNITARY CONTROLLERS</li>
      <li>HVAC &amp; PROCESS CONTROLS</li>
      <li>LIGHTING CONTROL</li>
      <li>CARD ACCESS</li>
      <li>COMMERCIAL &amp; INDUSTRIAL</li>
      <li class="cont">INSTALLATION WITH 24/7</li>
      <li class="cont">SERVICE</li>
    </ul>
    <svg class="abs" style="left:13px;top:432px" width="38" height="34" viewBox="0 0 38 34" fill="none" stroke="#fff" stroke-width="1.3">
      <circle cx="24" cy="13" r="9" stroke-dasharray="3 1.5"/><circle cx="24" cy="13" r="5.5"/>
      <polyline points="25,9 22.5,13.5 26,13.5 23,17.5"/>
      <path d="M2 33 v-6 a8 8 0 0 1 16 0 v6"/><path d="M4 18 a6 6 0 0 1 12 0 z"/>
    </svg>
    <div class="abs" style="left:55px;top:433px;width:1px;height:33px;background:#fff"></div>
    <div class="abs svc-cat" style="left:71px;top:437px">ELECTRICAL</div>
    <ul class="abs svc-list" style="top:481px">
      <li>GENERATOR INSTALLATIONS</li>
      <li>LIGHTING UPGRADES</li>
      <li>SERVICE UPGRADES</li>
      <li>VARIABLE FREQUENCY DRIVES</li>
      <li>COMMERCIAL AND INDUSTRIAL</li>
      <li class="cont">INSTALLATION WITH 24/7</li>
      <li class="cont">SERVICE</li>
    </ul>
  </div>

  <div class="panel p3">
    <div class="abs heading" style="left:1px;top:32px">BENEFITS OF AN</div>
    <div class="abs heading" style="left:0;top:58px"><span class="tag" style="padding:5px 8px 6px">OPEN</span><span style="margin-left:9px">SYSTEM</span></div>
    <svg class="abs b-icon" style="top:112px" viewBox="0 0 20 20" fill="none" stroke="var(--red)" stroke-width="1.4"><circle cx="10" cy="7" r="3"/><path d="M4 17a6 6 0 0 1 12 0"/><circle cx="3" cy="9" r="2"/><circle cx="17" cy="9" r="2"/></svg>
    <div class="abs benefit" style="top:114px">INTEROPERABILITY</div>
    <svg class="abs b-icon" style="top:145px" viewBox="0 0 20 20" fill="none" stroke="var(--red)" stroke-width="1.4"><rect x="5" y="7" width="10" height="11" rx="1"/><path d="M7.5 7V5a2.5 2.5 0 0 1 5 0v2"/></svg>
    <div class="abs benefit" style="top:147px">VENDOR NEUTRALITY</div>
    <svg class="abs b-icon" style="top:181px" viewBox="0 0 20 20" fill="none" stroke="var(--red)" stroke-width="1.4"><circle cx="10" cy="10" r="2"/><line x1="10" y1="8" x2="10" y2="2"/><line x1="12" y1="11" x2="17" y2="14"/><line x1="8" y1="11" x2="3" y2="14"/><circle cx="10" cy="2" r="1"/><circle cx="17" cy="14" r="1"/><circle cx="3" cy="14" r="1"/></svg>
    <div class="abs benefit" style="top:183px">SCALABILITY</div>
    <svg class="abs b-icon" style="top:216px" viewBox="0 0 20 20" fill="none" stroke="var(--red)" stroke-width="1.4"><path d="M10 18V10L4 4M10 10l6-6"/><polyline points="4,8 4,4 8,4"/><polyline points="12,4 16,4 16,8"/></svg>
    <div class="abs benefit" style="top:218px">FLEXIBILITY</div>
    <svg class="abs b-icon" style="top:259px" viewBox="0 0 20 20" fill="none" stroke="var(--red)" stroke-width="1.4"><rect x="3" y="4" width="12" height="14" rx="1"/><line x1="6" y1="8" x2="12" y2="8"/><line x1="6" y1="11" x2="11" y2="11"/><path d="M18 6l-6 7-1 2 2-1 6-7z"/></svg>
    <div class="abs benefit" style="top:252px">EASE OF<br>INTEGRATION</div>
    <svg class="abs b-icon" style="top:296px" viewBox="0 0 20 20" fill="none" stroke="var(--red)" stroke-width="1.4"><rect x="3" y="7" width="14" height="11" rx="1"/><path d="M7 7l1-4h4l1 4"/><text x="6" y="16" font-size="7" fill="var(--red)" stroke="none" font-family="Montserrat,sans-serif">$</text><line x1="11" y1="11" x2="15" y2="11"/><line x1="11" y1="14" x2="15" y2="14"/></svg>
    <div class="abs benefit" style="top:298px">REDUCED COSTS</div>
  </div>
</section>

</body>
</html>
```